Exclusive Offer Verbalis December 2022

A design that includes the company logo company and the text set out below. It could be a season design (winter design). it is a short promo to be sent by email. It should express that the promotion is on translation services.

Title: ESPECIAL DICIEMBRE

Information:

10% Descuento del 13 al 16 de diciembre
8% Después del 13 y hasta el 24 de diciembre

En contenidos web, materiales publicitarios, catàlogos, textos legales, manuales y más.

+30 años de experiencia, ISO 17100, traductores nativos

Target Market(s)

B2B Spain - any company that needs translation services

Industry/Entity Type

Services and Translation

Requirements
Must have
• Please take into account our corporate style guide attached
Nice to have
• A design that suggests a special offer from a serious, professional, technological and solid translation company.
Should not have
• Typical Christmas stationery, colours that don't fit into our company design trend.

```html
<!DOCTYPE html>
<html lang="es">
<head>
<meta charset="UTF-8">
<title>Especial Diciembre — Verbalis</title>
<link href="https://fonts.googleapis.com/css2?family=Montserrat:wght@600;700;800&display=swap" rel="stylesheet">
<style>
  :root {
    --sky: #47699a;
    --ornament: #3d5d8f;
    --navy: #1f4478;
    --ink: #26497f;
    --white: #ffffff;
    --cloud-top: #eef1f3;
    --cloud-bottom: #a6b6bf;
  }
  html, body { margin: 0; padding: 0; overflow: hidden; background: var(--sky); }
  .promo {
    position: relative;
    width: 1187px;
    height: 1200px;
    overflow: hidden;
    background: var(--sky);
    font-family: "Montserrat", sans-serif;
    color: var(--white);
  }
  .cloud-band {
    position: absolute; left: 0; top: 0;
    width: 1187px; height: 260px;
    background: linear-gradient(to bottom, var(--cloud-top) 0%, var(--cloud-top) 45%, var(--cloud-bottom) 100%);
  }
  .title {
    position: absolute; left: 0; top: 22px; width: 100%;
    margin: 0; text-align: center;
    font-size: 88px; font-weight: 800; letter-spacing: 1px; line-height: 1.1;
    color: var(--ink);
  }
  .ornament {
    position: absolute; border-radius: 50%;
    background: radial-gradient(circle at 50% 45%, var(--ornament) 0%, var(--sky) 100%);
  }
  .ornament-first { left: 44px; top: 481px; width: 320px; height: 320px; }
  .ornament-second { left: 424px; top: 430px; width: 320px; height: 320px; }
  .ornament-third { left: 837px; top: 457px; width: 344px; height: 344px; }
  .rate, .note, .scope {
    position: absolute; margin: 0; text-align: center;
  }
  .rate { font-weight: 800; line-height: 1; letter-spacing: -3px; }
  .note, .scope { font-size: 31px; font-weight: 600; line-height: 33px; }
  .rate-first { left: 54px; top: 518px; width: 330px; font-size: 148px; }
  .note-first { left: 54px; top: 653px; width: 330px; }
  .rate-second { left: 434px; top: 471px; width: 320px; font-size: 150px; }
  .note-second { left: 434px; top: 620px; width: 320px; }
  .scope { left: 837px; top: 509px; width: 344px; font-size: 32px; line-height: 33.5px; }
  .credentials {
    position: absolute; left: 0; top: 838px; width: 100%;
    margin: 0; text-align: center;
    font-size: 49px; font-weight: 700; line-height: 57px;
  }
  .brand-card {
    position: absolute; left: 287px; top: 991px;
    width: 619px; height: 209px;
    background: var(--white);
    border-radius: 26px 26px 0 0;
  }
  .brand-mark {
    position: absolute; left: 60px; top: 48px;
    width: 100px; height: 100px; background: var(--navy);
  }
  .brand-name {
    position: absolute; left: 253px; top: 50px; margin: 0;
    font-size: 56px; font-weight: 700; color: var(--navy); letter-spacing: 1px; line-height: 1.1;
  }
  .brand-tagline {
    position: absolute; left: 250px; top: 128px; margin: 0;
    font-size: 17px; font-weight: 700; color: var(--navy); line-height: 1.3;
  }
</style>
</head>
<body>
<main class="promo">
  <div class="cloud-band" role="img" aria-label="Nubes de papel en tonos grises claros"></div>
  <h1 class="title">ESPECIAL DICIEMBRE</h1>

  <div class="ornament ornament-first" role="img" aria-label="Bola navideña colgante"></div>
  <div class="ornament ornament-second" role="img" aria-label="Bola navideña colgante"></div>
  <div class="ornament ornament-third" role="img" aria-label="Bola navideña colgante"></div>

  <p class="rate rate-first">10%</p>
  <p class="note note-first">Descuento del<br>13 al 16 de<br>diciembre</p>

  <p class="rate rate-second">8%</p>
  <p class="note note-second">Después del<br>13 y hasta el 24<br>de diciembre</p>

  <p class="scope">En<br>contenidos web,<br>materiales<br>publicitarios,<br>catálogos, textos<br>legales,<br>manuales<br>y más.</p>

  <p class="credentials">+30 años de experiencia,<br>ISO 17100, traductores nativos</p>

  <div class="brand-card">
    <div class="brand-mark"></div>
    <p class="brand-name">VERBALIS</p>
    <p class="brand-tagline">TRADUCCIÓN Y DOCUMENTACIÓN<br>MULTILINGÜE</p>
  </div>
</main>
</body>
</html>
```